Promotional brochure for educational consulting firm

Updates

Hi Designers!

Please do a 8.5 x 11 inch tri-fold brochure as well as a 8.5 x 11 inch half-fold brochure.  I appreciate black and white versions in addition to color.  Please take a look at my company's website for a better sense of the look and feel I am going for:  www.brightlarkco.org

Thanks!

Industry/Entity Type

Consulting

Colors
3176b5
85abd2
fcfbfd

```html
<!DOCTYPE html>
<html lang="en">
<head>
<meta charset="utf-8">
<title>Brightlark Associates – Tri-fold Brochure</title>
<link href="https://fonts.googleapis.com/css2?family=Montserrat:wght@500;600;700&family=Open+Sans:wght@400;600&display=swap" rel="stylesheet">
<style>
  :root{
    --blue:#3176b5;
    --blue-deep:#245b91;
    --blue-navy:#1d4f82;
    --blue-soft:#85abd2;
    --blue-pale:#b9cfe7;
    --paper:#fcfbfd;
    --ink-grey:#8a8d92;
    --stage:#e6e7ea;
  }
  *{box-sizing:border-box;margin:0;padding:0}
  html,body{width:1200px;height:1000px;overflow:hidden;background:var(--stage)}
  .brochure{
    position:absolute;left:60px;top:82px;width:1080px;height:836px;
    display:flex;box-shadow:0 10px 30px rgba(0,0,0,.18);
  }
  .panel{position:relative;width:360px;height:100%;overflow:hidden;background:var(--paper)}
  .panel + .panel{border-left:1px solid rgba(0,0,0,.08)}

  /* Contact panel */
  .photo{position:absolute;left:0;width:100%}
  .photo--pencils{top:0;height:560px;background:linear-gradient(160deg,#e9c7a6 0%,#d9485a 30%,#e8c840 52%,#6a4aa8 72%,#e98cae 100%)}
  .contact-band{position:absolute;left:0;bottom:0;width:100%;height:330px;background:var(--blue-deep);clip-path:polygon(0 18%,100% 0,100% 100%,0 100%)}
  .contact{position:absolute;left:40px;bottom:92px;color:#fff;font-family:'Open Sans',sans-serif}
  .contact h2{font-family:'Montserrat',sans-serif;font-weight:600;font-size:26px;margin-bottom:18px}
  .contact p{font-size:14px;line-height:1.9;font-weight:600}

  /* Brand lockup */
  .brand{position:absolute;top:0;left:0;width:100%;height:260px;background:linear-gradient(180deg,#fff,#eceef1);
    display:flex;flex-direction:column;align-items:center;justify-content:center;gap:6px;
    clip-path:ellipse(90% 100% at 50% 0)}
  .brand__mark{width:46px;height:46px;border-radius:50%;background:var(--blue)}
  .brand__name{font-family:'Montserrat',sans-serif;font-weight:700;font-size:19px;color:var(--blue);letter-spacing:.5px}
  .brand__tag{font-family:'Montserrat',sans-serif;font-weight:700;font-size:10px;color:var(--blue);letter-spacing:.6px;text-transform:uppercase}

  /* Middle panel */
  .photo--books{top:170px;height:330px;background:linear-gradient(135deg,#c99a5c 0%,#d84a3a 25%,#3f6fb0 45%,#e8d24a 62%,#7a4a9a 80%,#c99a5c 100%)}
  .lower{position:absolute;left:0;bottom:0;width:100%;height:350px;background:linear-gradient(180deg,var(--blue-soft),var(--blue-pale))}
  .lower::after{content:"";position:absolute;left:0;right:0;bottom:0;height:28px;background:var(--blue)}
  .quote{position:absolute;left:0;top:0;height:30px;padding:0 18px;background:var(--blue);color:#fff;
    font-family:'Open Sans',sans-serif;font-size:12px;font-weight:600;display:flex;align-items:center;
    clip-path:polygon(0 0,100% 0,94% 100%,0 100%)}
  .url-band{position:absolute;right:0;bottom:0;width:44px;height:350px;background:var(--blue);
    display:flex;align-items:center;justify-content:center}
  .url-band span{transform:rotate(-90deg);white-space:nowrap;color:#fff;font-family:'Montserrat',sans-serif;font-weight:600;font-size:17px;letter-spacing:1px}

  /* Cover panel */
  .photo--class{top:170px;height:330px;background:linear-gradient(135deg,#f1f2f4 0%,#d9c8b2 35%,#f2eab4 60%,#a9d3e4 100%)}
</style>
</head>
<body>
<main class="brochure">
  <section class="panel panel--contact">
    <div class="photo photo--pencils" role="img" aria-label="Close-up of sharpened coloured pencils"></div>
    <div class="contact-band"></div>
    <div class="contact">
      <h2>Contact Us</h2>
      <p>Dana Whitfield, Ed.D., CEO</p>
      <p>dana@brightlarkco.org</p>
      <p>tel 555.014.2730</p>
      <p>fax 555.014.2731</p>
    </div>
  </section>

  <section class="panel panel--back">
    <div class="photo photo--books" role="img" aria-label="Library shelves filled with colourful books"></div>
    <div class="brand">
      <div class="brand__mark"></div>
      <div class="brand__name">BRIGHTLARK ASSOCIATES LLC</div>
      <div class="brand__tag">Supporting Schools &amp; School Leaders</div>
    </div>
    <div class="lower">
      <div class="quote">~School leadership is 24/7/365.</div>
    </div>
    <div class="url-band"><span>www.brightlarkco.org</span></div>
  </section>

  <section class="panel panel--cover">
    <div class="photo photo--class" role="img" aria-label="Smiling students working at desks in a classroom"></div>
    <div class="brand">
      <div class="brand__mark"></div>
      <div class="brand__name">BRIGHTLARK ASSOCIATES LLC</div>
      <div class="brand__tag">Supporting Schools &amp; School Leaders</div>
    </div>
    <div class="lower">
      <div class="quote">~School leadership is 24/7/365.</div>
    </div>
  </section>
</main>
</body>
</html>
```